Design of labels for exciting new natural skincare products...natural deodorant

I need some labels designed for a range of natural skincare, initially a natural deodorant paste. i will be offering a range of fragrances so i want a basic idea that i can drop different colours / ingredients into easily.

Fragrances are:
1. Jasmine, Orange and Bergamot
2. Lavender & Bergamot
3. Peppermint & Tea tree
4. Unscented
5. Lime, Lemongrass & Ginger

I am a new startup and will be selling online and through a couple of specialty online stores. The final design should encompass our ethos which is clean and green, not fussy nor clinical but friendly and easily accessible. I like fresh, contemporary modern look referencing vintage aesthetics.

The idea is that these products are better for your body AND the environment, and we pledge to use no plastic to package or distribute our products. i like the use of contemporary pastels such as soft pinks, tans and green/blue/aquas, though am open to new ideas too. the logo (attached) appears in red but that should not necessarily be used. i also like black and white with touches of colour.

Target Market(s)

Eco aware, health concious consumers with a reasonable skincare budget.

Industry/Entity Type

Skin Care Product

Font styles to use
Serif
Sans Serif
Decorative

Colors
2eb6a2
b768aa
eea4c8
fabb94
85cae6
cfeae6
eaf2ce
000000
eaeaea

Requirements
Must have
• Labels are for a small glass jar - the dimensions are 2cm high only and wrapping around the jar - at least 10cm wide. i'm also going to be providing a smaller size so this needs to be able to scale down to 1.5cm high and 8cm wide.
• the logo (supplied)
• title: Natural Deodorant
• Subtitle: Orange, Jasmine & Bergamot
• 45g
• Ingredients: tapioca starch*, bicarbonate of soda, Coconut oil*, shea butter*, mango butter*, diatomaceous earth*, sweet almond oil*, vitamin e*, tea tree oil*, Sweet orange essential oil*, Jasmine essential oil*, Bergamot essential oil*.
• *Certified organic ingredient
• (DESIGNERS - PLEASE NOTE NOT ALL THE INGREDIENTS ARE ORGANIC, PLEASE LIST THEM WITH A STAR * IF I HAVE SUPPLIED IT, THEN *Certified organic ingredient BELOW IN SLIGHTLY SMALLER TEXT - THIS SERVES AS THE KEY FOR THE INGREDIENTS LIST)
• pebblewick.nz
• Massage a pea-sized amount onto clean, dry armpits for an odour-free day.
• If irritation develops discontinue use and contact Fern Hollow. (please italicise the company name)
Nice to have
• open to ideas - i am attaching some examples of designs i like, you'll notice i swing between plain black and white aesthetics and a more decorative look. In general i like the old "medicine bottle" look, with hand sketched illustrations. But i'm open to ideas!

```html
<!DOCTYPE html>
<html lang="en">
<head>
<meta charset="utf-8">
<title>Fern Hollow — Natural Deodorant Label</title>
<link rel="stylesheet" href="https://fonts.googleapis.com/css2?family=Marcellus&family=Libre+Baskerville:ital,wght@1,700&family=Arimo&family=Roboto+Condensed&display=swap">
<style>
  :root {
    --backdrop: #e4e4e4;
    --label-top: #ffffff;
    --label-bottom: #e5eef2;
    --brand-blue: #b8d9e3;
    --title-pink: #deb0c3;
    --ink: #222222;
    --rule: #555555;
    --leaf-green: #3f9b4a;
    --badge-green: #2f8a3c;
    --dark-green: #1f5a2d;
  }
  html, body {
    margin: 0;
    padding: 0;
    width: 1200px;
    height: 1126px;
    overflow: hidden;
    background: var(--backdrop);
  }
  .canvas {
    position: relative;
    width: 1200px;
    height: 1126px;
  }
  .label {
    position: absolute;
    left: 0;
    top: 443px;
    width: 1500px;
    height: 300px;
    transform: scale(0.8);
    transform-origin: top left;
    background: linear-gradient(to bottom, var(--label-top) 0%, var(--label-top) 50%, var(--label-bottom) 100%);
    color: var(--ink);
  }
  .directions {
    position: absolute;
    left: 71px;
    top: 50px;
    font-family: "Arimo", Arial, sans-serif;
    font-size: 19px;
    letter-spacing: 0.7px;
    line-height: 22px;
  }
  .directions h3 {
    margin: 0;
    font-size: 20px;
    font-weight: 400;
  }
  .directions p { margin: 0; }
  .brand-name,
  .product-title,
  .fragrance {
    position: absolute;
    left: 0;
    width: 1536px;
    margin: 0;
    text-align: center;
    line-height: 1;
  }
  .brand-name {
    top: 36px;
    font-family: "Marcellus", serif;
    font-size: 62px;
    color: var(--brand-blue);
  }
  .product-title {
    top: 138px;
    font-family: "Marcellus", serif;
    font-weight: 400;
    font-size: 38px;
    color: var(--title-pink);
  }
  .fragrance {
    top: 186px;
    font-family: "Libre Baskerville", serif;
    font-style: italic;
    font-weight: 700;
    font-size: 19px;
    color: var(--ink);
  }
  .net-volume {
    position: absolute;
    left: 726px;
    top: 260px;
    font-family: "Roboto Condensed", sans-serif;
    font-size: 20px;
    line-height: 1;
    color: var(--ink);
  }
  .partner-badge {
    position: absolute;
    left: 832px;
    top: 232px;
  }
  .ingredients {
    position: absolute;
    left: 1109px;
    top: 66px;
    width: 380px;
    font-family: "Arimo", Arial, sans-serif;
  }
  .ingredients h3 {
    display: inline-block;
    margin: 0 0 4px;
    font-size: 17px;
    font-weight: 400;
    border-bottom: 1px solid var(--rule);
    padding-bottom: 1px;
  }
  .ingredients p {
    margin: 0;
    font-size: 14.5px;
    line-height: 19px;
    letter-spacing: 0.2px;
    white-space: nowrap;
  }
  .care-marks {
    position: absolute;
    left: 1110px;
    top: 204px;
  }
</style>
</head>
<body>
<main class="canvas">
  <section class="label">
    <div class="directions">
      <h3>To use:</h3>
      <p>For an odour-free day,<br>massage a pea sized amount<br>onto clean, dry underarms.</p>
    </div>

    <div class="brand-name">Fern Hollow</div>
    <h1 class="product-title">NATURAL DEODORANT</h1>
    <div class="fragrance">Orange - Jasmine - Bergamot</div>
    <div class="net-volume">60ml | 20z</div>

    <svg class="partner-badge" width="60" height="44" viewBox="0 0 60 44" role="img" aria-label="Partner certification badge">
      <circle cx="22" cy="22" r="20" fill="none" stroke="var(--leaf-green)" stroke-width="3"/>
    </svg>

    <div class="ingredients">
      <h3>Ingrediants</h3> :
      <p>Coconut oil*, tapioca starch*, bicarbonate of soda,<br>
      shea butter*, mango butter*, diatomaceous earth*,<br>
      sweet almond oil*, vitamin e*, tea tree oil*,<br>
      Sweet orange essential oil*, Jasmine essential oil*,<br>
      Bergamot essential oil*.</p>
    </div>

    <svg class="care-marks" width="310" height="80" viewBox="0 0 310 80" role="img" aria-label="Certification and care marks">
      <circle cx="36" cy="40" r="33" fill="none" stroke="var(--badge-green)" stroke-width="4"/>
      <rect x="86" y="8" width="64" height="64" rx="8" fill="none" stroke="var(--ink)" stroke-width="3"/>
      <circle cx="198" cy="40" r="31" fill="var(--dark-green)"/>
      <path d="M254 30 L302 6" stroke="var(--ink)" stroke-width="2" fill="none"/>
      <path d="M258 36 h44 v26 q-22 8 -44 0 z" fill="none" stroke="var(--ink)" stroke-width="1.5"/>
    </svg>
  </section>
</main>
</body>
</html>
```